Etiketten-Design für Frizzanteweine
Zielgruppe
Wir sind ein Weingut und suchen für unsere 3 Frizzanteweine ein neues elegantes, modernes Design.
Aufgabenstellung
Vorlage ist im Anhang zu finden.
Das Grundetikett ist weiß. Die Schriftart Frizzante wird mit Gold gedruckt.
Die 3 Etiketten sollen gleich sein und sich nur in der Hintergrundfarbe unterscheiden.
-> Watercolorhintergrund (Teile davon sollen beim Druck veredelt werden)
Auf den Flaschen sollte stehen:
1.Flasche: Frizzante trocken & Rosskamp mit Logo
HAUPTFARBE GRÜN
2.Flasche: Frizzante halbtrocken & Rosskamp mit Logo
HAUPTFARBE BLAU
3.Flasche: Frizzante Rosé & Rosskamp mit Logo
HAUPTFARBE ROSÈ
Etikettengröße: 9cm breit & 9cm hoch
Im Anhang findet man die Form der Flasche die wir verwenden.

```html
<!DOCTYPE html>
<html lang="de">
<head>
<meta charset="utf-8">
<title>Rosskamp Frizzante trocken – Etikett</title>
<link rel="stylesheet" href="https://fonts.googleapis.com/css2?family=Marcellus+SC&family=Kalam:wght@400&display=swap">
<style>
  :root {
    --label-white: #fdfdfd;
    --wash-green: #6fa583;
    --wash-green-light: #b9d6c3;
    --brand-green: #064a05;
    --silver-light: #e4e4e4;
    --silver-mid: #a9a9a9;
    --silver-dark: #8a8a8a;
  }
  html, body {
    margin: 0;
    padding: 0;
    width: 1200px;
    height: 1200px;
    overflow: hidden;
    background: var(--label-white);
  }
  .label {
    position: relative;
    width: 1200px;
    height: 1200px;
    background: var(--label-white);
    overflow: hidden;
  }
  .watercolor-wash {
    position: absolute;
    inset: 0;
    width: 1200px;
    height: 1200px;
  }
  .brand-mark {
    position: absolute;
    left: 415px;
    top: 163px;
    width: 362px;
    height: 362px;
    border-radius: 50%;
    background: var(--brand-green);
  }
  .brand-name {
    position: absolute;
    left: 0;
    width: 1200px;
    top: 548px;
    margin: 0;
    text-align: center;
    font-family: "Marcellus SC", serif;
    font-weight: 400;
    font-size: 58px;
    letter-spacing: 3px;
    color: var(--brand-green);
    line-height: 1;
  }
  .wine-type {
    position: absolute;
    left: 0;
    width: 1200px;
    top: 815px;
    margin: 0;
    text-align: center;
    font-family: "Marcellus SC", serif;
    font-weight: 400;
    font-size: 140px;
    letter-spacing: 10px;
    line-height: 1;
    background: linear-gradient(180deg, var(--silver-light) 0%, var(--silver-mid) 45%, var(--silver-light) 70%, var(--silver-dark) 100%);
    -webkit-background-clip: text;
    background-clip: text;
    color: transparent;
  }
  .sweetness {
    position: absolute;
    left: 0;
    width: 1200px;
    top: 1008px;
    margin: 0;
    text-align: center;
    font-family: "Kalam", cursive;
    font-size: 40px;
    color: var(--brand-green);
    line-height: 1;
  }
</style>
</head>
<body>
  <main class="label">
    <svg class="watercolor-wash" viewBox="0 0 1200 1200" role="img" aria-label="Weicher grüner Aquarell-Bogen als Hintergrund des Etiketts">
      <defs>
        <filter id="wash-blur" x="-20%" y="-20%" width="140%" height="140%">
          <feGaussianBlur stdDeviation="38"/>
        </filter>
      </defs>
      <path d="M620 110 C 320 120, 110 300, 150 560 C 190 820, 420 1000, 700 1090 C 800 1120, 860 1110, 880 1080"
            fill="none" stroke="var(--wash-green-light)" stroke-width="150" stroke-linecap="round"
            filter="url(#wash-blur)" opacity="0.75"/>
      <path d="M250 420 C 220 620, 320 820, 560 980 C 660 1040, 740 1060, 800 1060"
            fill="none" stroke="var(--wash-green)" stroke-width="70" stroke-linecap="round"
            filter="url(#wash-blur)" opacity="0.45"/>
    </svg>

    <div class="brand-mark" aria-hidden="true"></div>
    <h1 class="brand-name">Rosskamp</h1>

    <h2 class="wine-type">Frizzante</h2>
    <p class="sweetness">trocken</p>
  </main>
</body>
</html>
```